Buch-/E-Book-Cover für Sachbuch über Hunderasse
Zielgruppe
Ich benötige ein Buch-Cover im DIN A5 Format für ein anspruchsvolles Sachbuch, das die rassetypischen Krankheiten der Hunderasse Rhodesian Ridgeback thematisiert. Die Zielgruppe sind Züchter, Tierärzte und Liebhaber der Rasse.
Aufgabenstellung
Den größten Raum sollte ein Foto der Rasse einnehmen. Das Foto würde ich stellen, im Entwurf kann also ein Beispielfoto verwendet werden. Da das Buch der Auftakt zu einer Reihe ist, sollte das Design einen hohen Wiedererkennungswert haben und in erster Linie seriös wirken. Das Foto, der Rassename und die verwendeten Farben sollten leicht austauschbar sein. Sowohl der Titel als auch der Untertitel sind recht lang. Der Arbeitstitel lautet: Stille Pfade im Nebel der Ostseeküste, Untertitel: Geschichten von Fischern und Leuchttürmen.

```html
<!DOCTYPE html>
<html lang="de">
<head>
<meta charset="utf-8">
<title>Stille Pfade im Nebel der Ostseeküste – Umschlag</title>
<link href="https://fonts.googleapis.com/css2?family=Oswald:wght@400;500&family=Open+Sans:wght@400;600&display=swap" rel="stylesheet">
<style>
  :root {
    --stage: #ecebe8;
    --paper: #ffffff;
    --accent: #aac94a;
    --accent-spine: #b6d157;
    --ink: #1c1c1c;
    --on-accent: #ffffff;
    --portrait: #8a8f94;
    --portrait-light: #c9ccce;
    --hero-a: #b86a36;
    --hero-b: #8f4e24;
  }
  * { box-sizing: border-box; margin: 0; padding: 0; }
  html, body { width: 1200px; height: 705px; overflow: hidden; }
  body { background: var(--stage); font-family: "Open Sans", sans-serif; }

  .cover-spread {
    position: absolute; left: 151px; top: 52px;
    width: 898px; height: 600px;
    display: flex;
    box-shadow: 0 6px 24px rgba(0,0,0,.12);
  }

  /* back */
  .back-cover { position: relative; width: 424px; height: 600px; background: var(--paper); }
  .author-portrait {
    position: absolute; left: 50px; top: 60px; width: 140px; height: 170px;
    background: linear-gradient(160deg, var(--portrait-light), var(--portrait));
  }
  .blurb-upper {
    position: absolute; left: 190px; top: 100px; width: 205px; height: 130px;
    background: var(--accent); padding: 30px 12px 6px 16px;
  }
  .blurb-lower {
    position: absolute; left: 110px; top: 230px; width: 285px; height: 255px;
    background: var(--accent); padding: 6px 12px 10px 12px;
  }
  .blurb-upper p, .blurb-lower p {
    color: var(--on-accent); font-size: 8.6px; line-height: 12.4px;
    text-align: justify; hyphens: auto;
  }
  .blurb-lower p + p { margin-top: 2px; }

  /* spine */
  .spine {
    position: relative; width: 50px; height: 600px; background: var(--accent-spine);
  }
  .spine-title {
    position: absolute; left: 50%; top: 270px;
    transform: translate(-50%, -50%) rotate(-90deg);
    white-space: nowrap;
    font-family: "Oswald", sans-serif; font-weight: 400; font-size: 24px;
    letter-spacing: .3px; color: var(--on-accent);
  }
  .spine-title strong { font-weight: 500; text-transform: uppercase; }
  .spine-imprint {
    position: absolute; left: 0; right: 0; bottom: 28px; text-align: center;
    font-family: "Oswald", sans-serif; font-weight: 500; font-size: 9px;
    line-height: 10px; color: var(--ink); letter-spacing: .3px;
  }

  /* front */
  .front-cover { position: relative; width: 424px; height: 600px; background: var(--paper); overflow: hidden; }
  .front-title {
    position: absolute; right: 24px; top: 40px; text-align: right;
    font-family: "Oswald", sans-serif; color: var(--accent);
  }
  .front-title .lead { display: block; font-size: 34px; line-height: 42px; font-weight: 500; text-transform: uppercase; letter-spacing: .5px; }
  .front-title .lead small { font-size: 30px; text-transform: none; font-weight: 400; }
  .front-title .rest { display: block; font-size: 29px; line-height: 36px; font-weight: 400; }
  .hero-photo {
    position: absolute; left: 0; right: 0; top: 200px; height: 265px;
    background: radial-gradient(ellipse at 60% 50%, var(--hero-a), var(--hero-b) 75%, #f4f1ee 100%);
  }
  .front-subtitle {
    position: absolute; left: 30px; bottom: 40px;
    font-family: "Oswald", sans-serif; font-weight: 400; font-size: 20px;
    line-height: 27px; color: var(--accent);
  }
  .front-imprint {
    position: absolute; right: 26px; bottom: 48px; text-align: center;
    font-family: "Oswald", sans-serif; font-weight: 500; font-size: 13px;
    line-height: 14px; color: var(--ink); letter-spacing: .4px;
  }
  .front-imprint .mark { display: block; width: 14px; height: 14px; margin: 0 auto 6px; background: var(--ink); }
</style>
</head>
<body>
  <main class="cover-spread">
    <section class="back-cover">
      <div class="author-portrait" role="img" aria-label="Porträtfoto des Autors"></div>
      <div class="blurb-upper">
        <p>In den 25 Jahren meiner selbständigen Arbeit als Hebamme, habe ich viele Familien im Wochenbett betreut und dabei einen reichen Erfahrungsschatz gesammelt. Meine häufigsten Kunden waren natürlich Familien, die das erste Kind bekommen haben.</p>
      </div>
      <div class="blurb-lower">
        <p>Dies war zu der Zeit, als gerade der Krankenhausaufenthalt nach einer Spontangeburt von zehn auf sieben Tage gekürzt worden war. Die Krankenkasse bezahlte im Anschluss daran vier Tage Hebammen-Betreuung. Wenn die Familie diverse schwierige Themenfelder hatte, übernahm die Kasse die Kosten auch länger.</p>
        <p>Da ich meinen Beruf liebte, nahm ich mir für den Wochenbettbesuch auch immer genügend Zeit. Meist war eine Stunde nötig, manchmal jedoch waren so viele Fragen oder Irritationen (Unklarheiten), daß ich länger blieb. Auf die frisch gebackenen Eltern kommen unzählige unbekannte Situationen zu, die total verunsichern können. Auch bei sehr einfühlsamer Betreuung im Krankenhaus stellen sich viele Fragen erst zu Hause. Nämlich dann, wenn der Alltag mit dem Baby beginnt.</p>
      </div>
    </section>

    <section class="spine">
      <div class="spine-title"><strong>Stille Pfade</strong> im Nebel der Ostseeküste</div>
      <div class="spine-imprint">STRAND<br>HAFER</div>
    </section>

    <section class="front-cover">
      <h1 class="front-title">
        <span class="lead"><small>Stille</small> PFADE IM NEBEL</span>
        <span class="rest">der Ostseeküste</span>
      </h1>
      <div class="hero-photo" role="img" aria-label="Großes Titelfoto der Buchreihe"></div>
      <p class="front-subtitle">Geschichten von Fischern<br>und Leuchttürmen</p>
      <div class="front-imprint"><span class="mark"></span>STRAND<br>HAFER</div>
    </section>
  </main>
</body>
</html>
```